Cash For clothes textile recycling company leaflet design

We need flyer design for textile recycling company called RK BRIGHTFOLD LTD , we pay cash for peoples unwanted clothes and helping enviroment by moving used unwanted clothing to other countries in need, we are not charity company,as we pay money for people for their unwanted clothing. We would like to see designs that use yellow pink and bright green collors (more summer themes) you can use one or few logos we have uploaded

Industry/Entity Type

Textile

Font styles to use
Decorative

Colors
fbee3d
e34197
33a6d7
abd036
a54499
fece3e

Requirements
Nice to have
• you can play with logos, everything can be colourful, more soft colours, people shouldn't be pushed away from reading the leaflet, some sort of logos with smiles or so can appear as well
Should not have
• no big notes or cash pictures (can be something small) nothing dark or sad looking.

```html
<!DOCTYPE html>
<html lang="en">
<head>
<meta charset="utf-8">
<title>RK Brightfold Ltd – Cash for Clothes Leaflet</title>
<link rel="stylesheet" href="https://fonts.googleapis.com/css2?family=Nunito+Sans:wght@400;600;700;800&family=Arimo:wght@400;700&display=swap">
<style>
  :root {
    --page-bg: #e1e1e1;
    --paper: #ffffff;
    --ink: #1d1d1f;
    --green: #10a94b;
    --pink: #e8088f;
    --blue: #1a75bc;
    --sky-top: #c5dcf2;
    --sky-mid: #e6f2fb;
    --grass: #a9c57a;
  }
  * { box-sizing: border-box; margin: 0; padding: 0; }
  html, body { width: 1200px; height: 1000px; overflow: hidden; }
  body { background: var(--page-bg); font-family: "Nunito Sans", Arial, sans-serif; color: var(--ink); position: relative; }

  .leaflet { position: absolute; left: 138px; top: 126px; width: 922px; height: 712px; background: var(--paper); overflow: hidden; }

  .headline { position: absolute; top: 22px; left: 0; width: 100%; text-align: center; font-size: 40px; font-weight: 400; letter-spacing: 0.2px; }
  .headline .cash { color: var(--green); font-weight: 800; }
  .headline .unwanted { color: var(--pink); font-weight: 800; }

  .hero { position: absolute; left: 0; top: 80px; width: 922px; height: 567px;
    background: linear-gradient(180deg, var(--sky-top) 0%, var(--sky-mid) 55%, #eef6fb 80%, var(--grass) 100%); }
  .hero-sky-right { position: absolute; left: 470px; top: 0; width: 452px; height: 567px;
    background: radial-gradient(ellipse at 60% 20%, #9fcdf0 0%, #5aa6de 50%, #3f8fd0 100%); border-top-left-radius: 60% 100%; }
  .clothes-pile { position: absolute; left: 420px; top: 150px; width: 502px; height: 417px;
    border-top-left-radius: 55% 70%; border-top-right-radius: 40% 40%;
    background: linear-gradient(180deg, #e6d84a 0%, #d9a23c 18%, #c94a6a 34%, #7fb3d8 52%, #3b5fa8 70%, #5a3f8a 86%, #3a3a62 100%); }

  .brand-mark { position: absolute; left: 590px; top: 160px; display: flex; align-items: center; gap: 8px;
    background: var(--paper); padding: 8px 14px; border-radius: 24px; }
  .brand-mark .dot { width: 16px; height: 16px; border-radius: 50%; background: var(--green); }
  .brand-mark .name { font-size: 20px; font-weight: 800; color: var(--green); }

  .offer { position: absolute; left: 34px; top: 32px; width: 402px; text-align: center; }
  .rate { font-size: 33px; font-weight: 400; }
  .rate strong { color: var(--pink); font-weight: 800; }
  .call-pill { margin-top: 14px; height: 62px; border-radius: 31px; background: var(--green); color: #fff;
    font-size: 37px; font-weight: 800; line-height: 62px; letter-spacing: 0.5px; }
  .email { margin-top: 10px; display: flex; justify-content: center; align-items: center; gap: 10px; font-size: 19px; font-weight: 700; }
  .blurb { margin-top: 10px; font-size: 16.5px; line-height: 22px; }

  .policy { position: absolute; left: 34px; top: 307px; width: 402px; font-family: "Arimo", Arial, sans-serif; text-align: center; }
  .policy h3 { font-family: "Nunito Sans", Arial, sans-serif; font-size: 17px; font-weight: 800; }
  .accept { background: rgba(255,255,255,0.92); height: 82px; padding-top: 10px; font-size: 16.5px; line-height: 19px; }
  .reject { background: var(--pink); color: #fff; height: 137px; padding-top: 8px; font-size: 15.5px; line-height: 18px; }

  .tagline { position: absolute; background: var(--paper); font-size: 27px; font-weight: 400; white-space: nowrap; padding: 0 12px; line-height: 40px; }
  .tagline b { font-weight: 800; }
  .t1 { left: 530px; top: 257px; transform: rotate(-1deg); }
  .t1 b, .t2 b { color: var(--green); }
  .t2 { left: 512px; top: 298px; transform: rotate(-3.5deg); }
  .t3 { left: 497px; top: 356px; font-size: 24px; }
  .t4 { left: 468px; top: 398px; transform: rotate(-4deg); }
  .t4 b { color: var(--blue); }

  .footer { position: absolute; left: 0; top: 660px; width: 100%; text-align: center; font-size: 19px; letter-spacing: 0.2px; }
  .footer strong { font-weight: 800; }
</style>
</head>
<body>
  <main class="leaflet">
    <h1 class="headline">WE PAY <span class="cash">CASH</span> FOR YOUR <span class="unwanted">UNWANTED CLOTHES</span></h1>

    <section class="hero">
      <div class="hero-sky-right" role="img" aria-label="Bright blue summer sky with sunlight"></div>
      <div class="clothes-pile" role="img" aria-label="Large colourful pile of donated clothes on grass"></div>

      <div class="brand-mark"><span class="dot"></span><span class="name">RK BRIGHTFOLD</span></div>

      <div class="offer">
        <p class="rate">We will pay <strong>55p per kg</strong></p>
        <div class="call-pill">Call: 07700900482</div>
        <p class="email">
          <svg width="28" height="20" viewBox="0 0 28 20" aria-hidden="true"><rect x="1" y="1" width="26" height="18" fill="none" stroke="#1d1d1f" stroke-width="2"/><path d="M1 1 L14 11 L27 1" fill="none" stroke="#1d1d1f" stroke-width="2"/></svg>
          brightfold4417@mailbox.com
        </p>
        <p class="blurb">to arrange collection, and our helpful and friendly staff will make sure that your unwanted clothing will be collected as soon as possible, and pay you cash straight away!</p>
      </div>

      <div class="policy">
        <div class="accept">
          <h3>WE ACCEPT</h3>
          <p>Any clean dry clothing; Paired shoes; Belts<br>; Handbags;</p>
        </div>
        <div class="reject">
          <h3>WE DONT ACCEPT</h3>
          <p>Bad quality, wet, stained, mouldy or ripped items;<br>Used socks, underwear; Quits, duvets, pillows;<br>Bedding, curtains; Carpets, mats, rugs;<br>Books; CDs, DVDs, audio and video tapes;<br>Glass, metal, wood.</p>
        </div>
      </div>

      <p class="tagline t1">WE <b>RECYCLE CLOTHES</b></p>
      <p class="tagline t2">&amp; HELPING <b>ENVIRONMENT</b></p>
      <p class="tagline t3">MOVING UNWANTED CLOTHES</p>
      <p class="tagline t4">TO OTHER <b>COUNTRIES IN NEED</b></p>
    </section>

    <footer class="footer"><strong>RK BRIGHTFOLD LTD .</strong> REGISTERED IN ENGLAND &amp; WALES . COMPANY NUMBER: 08316274</footer>
  </main>
</body>
</html>
```